TRV Business Card

Business card design for a handyman company. Want to portray a professional image and stay away from the "Mom & Pops" image that is normally associated with handyman companies.

Business

```html
<!DOCTYPE html>
<html lang="en">
<head>
<meta charset="utf-8">
<title>TRV Business Card</title>
<link href="https://fonts.googleapis.com/css2?family=Questrial&family=Archivo:wght@600&display=swap" rel="stylesheet">
<style>
  :root {
    --backdrop: #e8e8e8;
    --card: #ffffff;
    --navy: #0a1e3a;
    --ink: #14223a;
    --white: #ffffff;
  }
  * { box-sizing: border-box; margin: 0; padding: 0; }
  html, body { width: 1200px; height: 1000px; overflow: hidden; }
  body {
    background: var(--backdrop);
    position: relative;
    font-family: "Questrial", "Helvetica Neue", Arial, sans-serif;
    color: var(--ink);
  }
  .card {
    position: absolute;
    top: 350px;
    width: 517px;
    height: 303px;
    background: var(--card);
    overflow: hidden;
  }
  .card--front { left: 72px; }
  .card--back { left: 622px; }

  .brand-name {
    font-family: "Questrial", "Helvetica Neue", Arial, sans-serif;
    color: var(--navy);
    font-size: 60px;
    line-height: 1;
    letter-spacing: 6px;
  }
  .card--front .brand-name {
    position: absolute;
    left: 30px;
    top: 34px;
  }

  .contact-list {
    position: absolute;
    left: 30px;
    top: 140px;
    list-style: none;
    font-size: 14.5px;
  }
  .contact-list li {
    display: flex;
    align-items: center;
    height: 26.5px;
  }
  .contact-list svg { width: 16px; height: 14px; margin-right: 10px; fill: var(--navy); }
  .contact-list .address { padding-left: 0; }

  .service-list {
    position: absolute;
    left: 335px;
    top: 114px;
    height: 126px;
    border-left: 2px solid var(--navy);
    padding-left: 11px;
  }
  .service-list h2 {
    font-weight: 400;
    font-size: 16px;
    margin-bottom: 4px;
  }
  .service-list ul { list-style: none; font-size: 14.5px; }
  .service-list li {
    height: 22px;
    display: flex;
    align-items: center;
  }
  .service-list li::before {
    content: "";
    width: 7px;
    height: 7px;
    background: var(--navy);
    margin-right: 10px;
  }

  .tagline {
    font-family: "Archivo", Arial, sans-serif;
    font-weight: 600;
    font-size: 15px;
    text-transform: uppercase;
    white-space: nowrap;
  }
  .card--front .tagline-band {
    position: absolute;
    left: 0; bottom: 0;
    width: 100%;
    height: 47px;
    background: var(--navy);
    color: var(--white);
    display: flex;
    align-items: center;
    justify-content: center;
  }

  .accent-bar {
    position: absolute;
    top: 131px;
    height: 41px;
    background: var(--navy);
  }
  .accent-bar--left { left: 0; width: 91px; }
  .accent-bar--right { right: 0; width: 92px; }
  .card--back .brand-name {
    position: absolute;
    left: 91px; right: 92px;
    top: 120px;
    text-align: center;
    font-size: 62px;
  }
  .card--back .tagline {
    position: absolute;
    left: 0; right: 0;
    top: 187px;
    text-align: center;
    color: var(--navy);
  }
</style>
</head>
<body>
  <section class="card card--front" aria-label="Card front">
    <div class="brand-name">TRV</div>

    <ul class="contact-list">
      <li>
        <svg viewBox="0 0 16 14" aria-hidden="true"><path d="M1 4c0-2 2-3 7-3s7 1 7 3v1h-3V4H4v1H1zM4 6h8l2 7H2z"/></svg>
        (555) 014-2710
      </li>
      <li>
        <svg viewBox="0 0 16 14" aria-hidden="true"><path d="M4 0h8v4H4zM1 5h14v6h-3v3H4v-3H1zM5 9v4h6V9z"/></svg>
        (555) 014-3385
      </li>
      <li>
        <svg viewBox="0 0 16 14" aria-hidden="true"><path d="M1 2h14v1L8 8 1 3zM1 5l7 5 7-5v7H1z"/></svg>
        info@trvservices.com
      </li>
      <li class="address">4270 W Meadow Ln Riverton, Ks 66000</li>
    </ul>

    <div class="service-list">
      <h2>Potential Verbage :</h2>
      <ul>
        <li>Home Repairs</li>
        <li>Handyman</li>
        <li>Services</li>
        <li>Drain Cleaning</li>
        <li>Carpet Cleaning</li>
      </ul>
    </div>

    <div class="tagline-band"><span class="tagline">Residential &amp; Commercial Services</span></div>
  </section>

  <section class="card card--back" aria-label="Card back">
    <div class="accent-bar accent-bar--left"></div>
    <div class="accent-bar accent-bar--right"></div>
    <div class="brand-name">TRV</div>
    <div class="tagline">Residential &amp; Commercial Services</div>
  </section>
</body>
</html>
```